Breezeway Comfort business cards design

Need a business card design for a Heating and Air Conditioning business. I need these items included.
Business name: Breezeway Comfort
Owner: Marcus Tollefsen
License # 2874590
Phone number # 555-382-4071
Email: breezewaycomfortair@mailvista.example
Sales
Service
Installation
Maintenance

Heating and Air Conditioning

Requirements
Must have
• Company name , license number , phone number , email

```html
<!DOCTYPE html>
<html lang="en">
<head>
<meta charset="utf-8">
<title>Breezeway Comfort – Business Cards</title>
<link rel="stylesheet" href="https://fonts.googleapis.com/css2?family=Exo+2:wght@600;700;800&family=Roboto:wght@400&display=swap">
<style>
  :root {
    --stage: #4d4d4f;
    --card: #ffffff;
    --blue: #0a3ca5;
    --orange: #f48b32;
    --red: #ea3a3a;
    --ink: #333333;
    --label: #e6e6e6;
  }
  * { margin: 0; padding: 0; box-sizing: border-box; }
  html, body { width: 1200px; height: 1200px; overflow: hidden; background: var(--stage); }
  .presentation { position: relative; width: 1200px; height: 1200px; background: var(--stage); border: 1px solid #2b2b2b; }
  .card { position: absolute; left: 182px; width: 840px; height: 481px; background: var(--card); overflow: hidden; font-family: "Exo 2", sans-serif; }
  .card--front { top: 74px; }
  .card--back { top: 649px; }
  .card-art { position: absolute; inset: 0; width: 840px; height: 481px; }
  .side-label { position: absolute; left: 0; width: 1200px; text-align: center; font-family: "Roboto", sans-serif; font-size: 18px; color: var(--label); }
  .side-label--front { top: 604px; }
  .side-label--back { top: 1150px; }

  .owner { position: absolute; left: 497px; top: 71px; height: 40px; padding-left: 19px; border-left: 7px solid var(--blue); color: var(--ink); width: 273px; }
  .owner-name { font-weight: 700; font-size: 30px; line-height: 30px; letter-spacing: 0.3px; }
  .owner-role { font-weight: 700; font-size: 15px; line-height: 14px; text-align: right; }

  .brand-name { position: absolute; color: var(--blue); font-weight: 800; text-transform: uppercase; letter-spacing: 3px; }
  .card--front .brand-name { left: 302px; top: 172px; font-size: 52px; line-height: 60px; }
  .card--back .brand-name { left: 0; width: 840px; top: 294px; text-align: center; font-size: 36px; }

  .contact { position: absolute; left: 0; width: 836px; top: 296px; text-align: center; color: var(--ink); font-weight: 700; font-size: 19px; line-height: 28px; }

  .services { position: absolute; left: 72px; top: 426px; display: flex; align-items: center; color: #fff; font-weight: 700; font-size: 22px; list-style: none; }
  .services li { padding: 0 12px; border-left: 3px solid var(--orange); line-height: 36px; }
  .services li:first-child { padding-left: 0; border-left: none; }
</style>
</head>
<body>
<main class="presentation">

  <section class="card card--front" aria-label="Business card front">
    <svg class="card-art" viewBox="0 0 840 481" aria-hidden="true">
      <defs>
        <linearGradient id="warm-tl" x1="0" y1="1" x2="1" y2="0">
          <stop offset="0" stop-color="#ea3a3a"/><stop offset="0.6" stop-color="#f48b32"/>
        </linearGradient>
        <linearGradient id="warm-br" x1="1" y1="0" x2="0" y2="1">
          <stop offset="0" stop-color="#ea3a3a"/><stop offset="0.6" stop-color="#f48b32"/>
        </linearGradient>
      </defs>
      <polygon points="0,0 190,0 0,174" fill="url(#warm-tl)"/>
      <polygon points="138,50 184,50 0,213 0,181" fill="var(--blue)"/>
      <polygon points="0,389 722,389 649,481 0,481" fill="var(--blue)"/>
      <polygon points="698,390 738,390 840,302 840,266" fill="var(--blue)"/>
      <polygon points="840,304 840,481 649,481" fill="url(#warm-br)"/>
      <circle cx="201" cy="229" r="62" fill="var(--orange)"/>
    </svg>

    <div class="owner">
      <p class="owner-name">Marcus Tollefsen</p>
      <p class="owner-role">Owner</p>
    </div>

    <h1 class="brand-name">Breezeway<br>Comfort</h1>

    <div class="contact">
      <p>License # 2874590</p>
      <p>Phone number # 555-382-4071</p>
      <p>Email: breezewaycomfortair@mailvista.example</p>
    </div>

    <ul class="services">
      <li>Sales</li>
      <li>Service</li>
      <li>Installation</li>
      <li>Maintenance</li>
    </ul>
  </section>
  <p class="side-label side-label--front">front</p>

  <section class="card card--back" aria-label="Business card back">
    <svg class="card-art" viewBox="0 0 840 481" aria-hidden="true">
      <defs>
        <linearGradient id="warm-band" x1="0" y1="1" x2="1" y2="0">
          <stop offset="0" stop-color="#ea3a3a"/><stop offset="0.45" stop-color="#f48b32"/>
        </linearGradient>
      </defs>
      <rect x="0" y="0" width="840" height="34" fill="url(#warm-band)"/>
      <polygon points="365,34 840,34 840,52 429,52" fill="var(--blue)"/>
      <polygon points="0,429 410,429 473,446 0,446" fill="url(#warm-band)"/>
      <rect x="0" y="446" width="840" height="35" fill="var(--blue)"/>
      <circle cx="420" cy="200" r="52" fill="var(--orange)"/>
    </svg>
    <h2 class="brand-name">Breezeway Comfort</h2>
  </section>
  <p class="side-label side-label--back">back</p>

</main>
</body>
</html>
```